Post storm repair flyer

looking for an eye catching 6x9 postcard to send out to single family home owners advertising a "Post Storm Repair Special" explaining that after the recent hurricanes its very important to have your roof checked and any repairs fixed right away before they become a bigger more costly problem and that even though your home wasn't directly hit by the storm the high wind gust could've cause unseen damage.
offer $200 off any repair *some rules may apply
Lark Roofing
888.417.LARK
www.LarkRoofing.example

Roofing

```html
<!DOCTYPE html>
<html lang="en">
<head>
<meta charset="utf-8">
<title>Lark Roofing – Post Storm Repair Special</title>
<link href="https://fonts.googleapis.com/css2?family=Poppins:wght@500;600;700;800&family=Roboto:wght@300;400&family=Anton&family=Sacramento&display=swap" rel="stylesheet">
<style>
  :root {
    --ink: #000000;
    --paper: #ffffff;
    --gold: #e9b43a;
    --charcoal: #1f1f1f;
    --backdrop: #d8d5ce;
  }
  * { margin: 0; padding: 0; box-sizing: border-box; }
  html, body {
    width: 1200px; height: 1200px; overflow: hidden;
    background: var(--backdrop);
  }
  .postcard {
    position: absolute; left: 222px; top: 40px;
    width: 756px; height: 1120px;
    background: var(--ink);
    overflow: hidden;
  }
  .postcard__shapes, .postcard__script { position: absolute; inset: 0; }
  .headline__line {
    position: absolute;
    font-family: "Poppins", sans-serif;
    font-weight: 800;
    font-size: 158px;
    line-height: 1;
    letter-spacing: -0.03em;
    white-space: nowrap;
  }
  .headline__line--post { left: 174px; top: 60px; color: var(--paper); }
  .headline__line--storm { left: 100px; top: 190px; color: var(--gold); }
  .headline__line--repair { left: 112px; top: 319px; color: var(--paper); }
  .headline__script {
    font-family: "Sacramento", cursive;
    font-size: 128px;
    fill: var(--gold);
  }
  .intro {
    position: absolute; left: 68px; top: 583px; width: 620px;
    font-family: "Roboto", sans-serif; font-weight: 300;
    font-size: 20px; line-height: 24px;
    color: var(--paper); text-align: center;
  }
  .brand {
    position: absolute; left: 19px; top: 888px; width: 400px;
    display: flex; align-items: center; justify-content: center; gap: 12px;
  }
  .brand__mark { width: 22px; height: 22px; background: var(--charcoal); }
  .brand__name {
    font-family: "Poppins", sans-serif; font-weight: 700;
    font-size: 32px; color: var(--charcoal); white-space: nowrap;
  }
  .website {
    position: absolute; left: 19px; top: 996px; width: 400px;
    font-family: "Poppins", sans-serif; font-weight: 500;
    font-size: 23px; letter-spacing: 0.02em;
    color: var(--charcoal); text-align: center;
  }
  .offer text { font-family: "Poppins", sans-serif; }
  .offer__label { font-weight: 700; font-size: 30px; fill: var(--paper); }
  .offer__amount { font-family: "Anton", sans-serif !important; font-size: 140px; fill: var(--ink); }
  .offer__dollar { font-family: "Anton", sans-serif !important; font-size: 66px; fill: var(--ink); }
  .offer__off { font-weight: 800; font-size: 44px; fill: var(--ink); }
  .offer__scope { font-weight: 700; font-size: 25px; fill: var(--ink); }
  .offer__terms { font-family: "Roboto", sans-serif !important; font-size: 12px; fill: var(--paper); }
</style>
</head>
<body>
<main class="postcard">
  <svg class="postcard__shapes" width="756" height="1120" viewBox="0 0 756 1120">
    <polygon class="house-band" points="0,864 232,716 756,1014 756,1120 0,1120" fill="var(--paper)"/>
    <path class="swoosh" d="M452,537 Q545,500 641,537 Q545,508 452,537 Z" fill="var(--paper)" stroke="var(--paper)" stroke-width="2"/>

    <g class="offer">
      <polygon points="550,729 697,814 697,985 550,1068 401,985 401,810" fill="var(--gold)" stroke="var(--ink)" stroke-width="1.5"/>
      <path d="M550,736 L630,783 Q590,795 550,820 Q510,795 469,783 Z" fill="var(--ink)"/>
      <text class="offer__label" x="550" y="790" text-anchor="middle">OFFER</text>
      <text class="offer__dollar" x="416" y="888">$</text>
      <text class="offer__amount" x="453" y="937" textLength="180" lengthAdjust="spacingAndGlyphs">200</text>
      <text class="offer__off" transform="translate(682,939) rotate(-90)" textLength="100" lengthAdjust="spacingAndGlyphs">OFF</text>
      <polygon points="455,943 652,943 662,959 652,976 455,976 445,959" fill="var(--paper)"/>
      <text class="offer__scope" x="552" y="969" text-anchor="middle">ANY REPAIR</text>
      <polygon points="550,992 616,1023 550,1061 484,1023" fill="var(--ink)"/>
      <text class="offer__terms" x="550" y="1011" text-anchor="middle">*</text>
      <text class="offer__terms" x="550" y="1026" text-anchor="middle">Some rules</text>
      <text class="offer__terms" x="550" y="1042" text-anchor="middle">may apply</text>
    </g>
  </svg>

  <h1 class="headline">
    <span class="headline__line headline__line--post">POST</span>
    <span class="headline__line headline__line--storm">STORM</span>
    <span class="headline__line headline__line--repair">REPAIR</span>
  </h1>

  <svg class="postcard__script" width="756" height="1120" viewBox="0 0 756 1120">
    <polygon class="bolt" points="619,300 666,274 641,394 661,384 648,437 656,386 636,394 658,286 619,326" fill="var(--gold)"/>
    <text class="headline__script" x="330" y="508" textLength="292" lengthAdjust="spacingAndGlyphs" transform="rotate(-11 330 508)">Special</text>
  </svg>

  <p class="intro">After the recent hurricanes its very important to have your roof checked and any repairs fixed right away before they become a bigger more costly problem and that even though your home wasn't directly hit by the storm the high wind gust could've cause unseen damage.</p>

  <div class="brand">
    <span class="brand__mark"></span>
    <span class="brand__name">Lark Roofing</span>
  </div>
  <p class="website">LARKROOFING.EXAMPLE</p>
</main>
</body>
</html>
```